Multi Academy Trust needs to shout about our vision by turning our words into something that can ...

Our vision is something we want to shout about and share through multiple media avenues to a range of stakeholders including parents, staff, pupils, other school trusts, Board of Scholastic Affairs and suppliers. We want an eye-catching design that stands out from the crowd but incorporates our current brand (and logo)

```html
<!DOCTYPE html>
<html lang="en">
<head>
<meta charset="utf-8">
<title>Northfield Learning Trust – Our Core Purpose</title>
<link rel="stylesheet" href="https://fonts.googleapis.com/css2?family=Saira:wght@700;800&family=Barlow:wght@400;600&display=swap">
<style>
  :root {
    --page: #ffffff;
    --brand-blue: #1b8fd2;
    --panel-blue: #9dd3ef;
    --logo-grey: #6d6e71;
    --ink: #1f1f1f;
    --white: #ffffff;
    --forest-dark: #1d2a1c;
    --forest-mid: #3f5a35;
    --moss-green: #8a9a3a;
    --moss-orange: #c9792e;
  }
  * { box-sizing: border-box; margin: 0; padding: 0; }
  html, body { width: 1155px; height: 1200px; overflow: hidden; background: var(--page); }
  body { position: relative; font-family: "Barlow", Arial, sans-serif; }

  .brand {
    position: absolute; top: 38px; left: 820px;
    display: flex; align-items: center; gap: 16px;
  }
  .brand-dot { width: 78px; height: 78px; border-radius: 50%; background: var(--brand-blue); flex: none; }
  .brand-name {
    font-family: "Barlow", Arial, sans-serif; font-weight: 400;
    font-size: 30px; line-height: 32px; color: var(--logo-grey);
  }

  .hero {
    position: absolute; left: 42px; top: 228px; width: 1064px; height: 664px;
    overflow: hidden;
  }
  .hero-photo {
    position: absolute; inset: 0;
    background:
      radial-gradient(ellipse 60% 40% at 70% 30%, rgba(190,210,200,.35), transparent 70%),
      linear-gradient(180deg, var(--forest-dark) 0%, var(--forest-mid) 45%, var(--moss-orange) 72%, var(--moss-green) 100%);
  }
  .hero-title {
    position: absolute; left: 62px; top: 26px;
    font-family: "Saira", Arial, sans-serif; font-weight: 700;
    font-size: 36px; letter-spacing: 0.5px; color: var(--white);
  }
  .hero-statement {
    position: absolute; left: 470px; top: 548px; width: 580px;
    font-family: "Saira", Arial, sans-serif; font-weight: 800;
    font-size: 19.5px; line-height: 29px; color: var(--white);
    white-space: nowrap;
  }

  .values {
    position: absolute; left: 42px; top: 904px; width: 1064px; height: 271px;
    background: var(--panel-blue); overflow: hidden;
  }
  .values-disc {
    position: absolute; left: 8px; top: 12px;
    width: 244px; height: 244px; border-radius: 50%;
    background: var(--brand-blue);
  }
  .values-heading {
    position: absolute; left: 455px; top: 18px;
    font-family: "Saira", Arial, sans-serif; font-weight: 700;
    font-size: 19px; color: var(--ink);
  }
  .values-list {
    position: absolute; left: 455px; top: 68px; width: 560px;
    list-style: none; counter-reset: value;
    font-size: 20px; line-height: 26.5px; color: var(--ink);
    white-space: nowrap;
  }
  .values-list li { counter-increment: value; padding-left: 28px; position: relative; }
  .values-list li::before { content: counter(value) "."; position: absolute; left: 0; }
</style>
</head>
<body>
  <header class="brand">
    <span class="brand-dot"></span>
    <div class="brand-name">Northfield<br>Learning<br>Trust</div>
  </header>

  <section class="hero">
    <div class="hero-photo" role="img" aria-label="Close-up photograph of a young green seedling rising from sunlit moss in a softly blurred forest"></div>
    <h1 class="hero-title">We have one core purpose:</h1>
    <p class="hero-statement">To have the biggest positive impact in the varied<br>communities we serve through ensuring top drawer<br>education for our learners. #ShapingFutures</p>
  </section>

  <section class="values">
    <span class="values-disc"></span>
    <h2 class="values-heading">In all we do we are:</h2>
    <ol class="values-list">
      <li>Ethical to the core, ensuring that education<br>is always front and centre</li>
      <li>Futures focused system leaders – never<br>simply followers</li>
      <li>Collaborative in every endeavour</li>
      <li>Resolutely learner centred.</li>
    </ol>
  </section>
</body>
</html>
```